iOS App Design Project for Pebble Notes

We are looking for a redesign of the UI for our app, Pebble Notes. The app is a to-do list type app with 4 screens, and we already have a UI for it but we would like a nicer looking one that has a better colour scheme and is more intuitive.

We would like something that is a real treat to look at, and that users really want to use. Essentially what we want is the nicest and most simple design possible, as the current UI we have is not very user friendly.

The app is already on the market and is free so if you have an iOS device you can download it and take a look at it, and we have also included screenshots of the app.
Updates

Project Deadline Extended
Reason: I am updating the design brief and will also guarantee the payment.

Target Market(s)

Mobile users looking for simplicity

Requirements
Must have
• - Very visually pleasing
- Simple layout with minimal clutter
- Icons and buttons that explain what they do
Should not have
• Any features that detract from the simplicity of the app are not wanted.

```html
<!DOCTYPE html>
<html lang="en">
<head>
<meta charset="utf-8">
<title>Pebble Notes – Task</title>
<link href="https://fonts.googleapis.com/css2?family=Arimo:wght@400;700&family=Open+Sans:ital,wght@1,300;1,400&display=swap" rel="stylesheet">
<style>
  :root {
    --status-top: #f4f4f4;
    --status-bottom: #c9c9c9;
    --nav-top: #b7c5d8;
    --nav-mid: #8ea2bf;
    --nav-bottom: #6f86a8;
    --nav-edge: #4e6584;
    --body-bg: #7a7b7d;
    --body-dot: #727375;
    --row-line: #e6e6e6;
    --text-white: #ffffff;
    --text-dark: #1a1a1a;
    --signal-blue: #2f6fd6;
    --toggle-blue: #2a6ee8;
    --toggle-blue-dark: #1a50b8;
    --tab-bg: #1c1c1c;
    --tab-bg-top: #3a3a3a;
    --tab-active: #3b3b3b;
    --tab-label: #9a9a9a;
    --tab-accent: #3cc6f0;
    --battery-green: #2fbf2f;
  }
  * { margin: 0; padding: 0; box-sizing: border-box; }
  html, body { width: 800px; height: 1200px; overflow: hidden; }
  body { font-family: "Arimo", Helvetica, Arial, sans-serif; background: var(--body-bg); }

  .app-screen { position: relative; width: 800px; height: 1200px; overflow: hidden; }

  .status-bar {
    position: absolute; left: 0; top: 0; width: 800px; height: 50px;
    background: linear-gradient(var(--status-top), var(--status-bottom));
    border-bottom: 1px solid #9a9a9a;
    color: var(--text-dark); font-weight: 700; font-size: 28px;
  }
  .status-bar .signal { position: absolute; left: 10px; top: 14px; }
  .status-bar .carrier { position: absolute; left: 62px; top: 9px; }
  .status-bar .network { position: absolute; left: 195px; top: 9px; color: var(--signal-blue); }
  .status-bar .clock { position: absolute; left: 0; width: 800px; top: 9px; text-align: center; }
  .status-bar .alarm { position: absolute; left: 622px; top: 12px; }
  .status-bar .battery-level { position: absolute; left: 664px; top: 9px; }
  .status-bar .battery { position: absolute; left: 740px; top: 13px; }

  .nav-bar {
    position: absolute; left: 0; top: 50px; width: 800px; height: 125px;
    background: linear-gradient(var(--nav-top) 0%, var(--nav-mid) 50%, var(--nav-bottom) 100%);
    border-bottom: 2px solid var(--nav-edge);
    box-shadow: 0 4px 8px rgba(0,0,0,0.25);
  }
  .nav-title {
    position: absolute; left: 0; width: 800px; top: 28px; text-align: center;
    color: var(--text-white); font-size: 50px; font-weight: 700;
    text-shadow: 0 -2px 0 rgba(0,0,0,0.4);
  }
  .back-button { position: absolute; left: 14px; top: 24px; }

  .task-list { position: absolute; left: 0; top: 175px; width: 800px; height: 906px;
    background-image: radial-gradient(var(--body-dot) 1px, transparent 1.5px);
    background-size: 6px 6px; }

  .task-row { position: absolute; left: 0; top: 170px; width: 800px; height: 90px; }
  .task-row .disclosure { position: absolute; left: 20px; top: 20px; }
  .task-row .task-name {
    position: absolute; left: 112px; top: 14px;
    font-family: "Open Sans", Helvetica, Arial, sans-serif; font-style: italic; font-weight: 300;
    font-size: 56px; color: var(--text-white);
  }
  .toggle {
    position: absolute; left: 537px; top: 175px; width: 228px; height: 71px;
    border-radius: 12px; overflow: hidden; border: 2px solid #5a5a5a;
    background: linear-gradient(var(--toggle-blue-dark), var(--toggle-blue) 50%, #4a8af0);
  }
  .toggle .toggle-label {
    position: absolute; left: 0; width: 132px; top: 14px; text-align: center;
    color: var(--text-white); font-weight: 700; font-size: 34px;
  }
  .toggle .toggle-knob {
    position: absolute; right: 0; top: 0; width: 98px; height: 100%;
    border-radius: 10px; background: linear-gradient(#d8d8d8, #ffffff 40%, #f0f0f0);
    border-left: 1px solid #9a9a9a;
  }

  .row-line {
    position: absolute; left: 160px; width: 480px; height: 2px;
    background: linear-gradient(90deg, transparent, var(--row-line) 25%, var(--row-line) 75%, transparent);
  }

  .add-button { position: absolute; left: 341px; top: 975px; }

  .tab-bar {
    position: absolute; left: 0; top: 1081px; width: 800px; height: 119px;
    background: linear-gradient(var(--tab-bg-top) 0%, var(--tab-bg) 50%, #000 51%, #0a0a0a 100%);
  }
  .tab { position: absolute; top: 6px; width: 190px; height: 107px; text-align: center; }
  .tab.is-active { background: var(--tab-active); border-radius: 6px; }
  .tab svg { position: absolute; left: 50%; top: 6px; transform: translateX(-50%); }
  .tab .tab-label {
    position: absolute; left: 0; width: 100%; bottom: 2px;
    color: var(--tab-label); font-weight: 700; font-size: 25px;
  }
  .tab.is-active .tab-label { color: var(--text-white); }
</style>
</head>
<body>
<div class="app-screen">

  <header class="status-bar">
    <svg class="signal" width="48" height="22" viewBox="0 0 48 22">
      <rect x="0" y="14" width="7" height="8" fill="var(--signal-blue)"/>
      <rect x="9" y="11" width="7" height="11" fill="var(--signal-blue)"/>
      <rect x="18" y="8" width="7" height="14" fill="var(--signal-blue)"/>
      <rect x="27" y="19" width="7" height="3" fill="var(--signal-blue)"/>
      <rect x="36" y="19" width="7" height="3" fill="var(--signal-blue)"/>
    </svg>
    <span class="carrier">Wattle</span>
    <span class="network">3G</span>
    <span class="clock">12:53 PM</span>
    <svg class="alarm" width="26" height="26" viewBox="0 0 26 26">
      <circle cx="13" cy="13" r="12" fill="#555"/>
      <path d="M13 6 V13 H18" stroke="#ddd" stroke-width="2.5" fill="none"/>
    </svg>
    <span class="battery-level">81 %</span>
    <svg class="battery" width="52" height="26" viewBox="0 0 52 26">
      <rect x="1" y="1" width="44" height="24" rx="3" fill="#fff" stroke="#222" stroke-width="2"/>
      <rect x="4" y="4" width="38" height="18" fill="var(--battery-green)"/>
      <rect x="46" y="8" width="5" height="10" fill="#222"/>
      <path d="M26 4 L16 14 H23 L19 22 L31 11 H24 Z" fill="#111"/>
    </svg>
  </header>

  <nav class="nav-bar">
    <svg class="back-button" width="126" height="74" viewBox="0 0 126 74">
      <defs>
        <linearGradient id="back-fill" x1="0" y1="0" x2="0" y2="1">
          <stop offset="0" stop-color="#8aa1c2"/>
          <stop offset="0.5" stop-color="#6a84aa"/>
          <stop offset="1" stop-color="#58729a"/>
        </linearGradient>
      </defs>
      <path d="M3 37 L30 3 H116 Q124 3 124 11 V63 Q124 71 116 71 H30 Z" fill="url(#back-fill)" stroke="#3f5473" stroke-width="2"/>
      <text x="74" y="48" text-anchor="middle" font-family="Arimo, Helvetica, sans-serif" font-weight="700" font-size="31" fill="#fff">Back</text>
    </svg>
    <h1 class="nav-title">TASK</h1>
  </nav>

  <main class="task-list">
    <div class="task-row">
      <svg class="disclosure" width="60" height="60" viewBox="0 0 60 60">
        <circle cx="30" cy="30" r="28" fill="#fff"/>
        <circle cx="30" cy="30" r="23" fill="#2c6fd8"/>
        <path d="M25 18 L37 30 L25 42" stroke="#fff" stroke-width="7" fill="none" stroke-linecap="round" stroke-linejoin="round"/>
      </svg>
      <span class="task-name">Hello.....</span>
    </div>
    <div class="toggle">
      <span class="toggle-label">ON</span>
      <span class="toggle-knob"></span>
    </div>

    <div class="row-line" style="top:260px"></div>
    <div class="row-line" style="top:385px"></div>
    <div class="row-line" style="top:510px"></div>
    <div class="row-line" style="top:635px"></div>
    <div class="row-line" style="top:760px"></div>
  </main>

  <svg class="add-button" width="118" height="88" viewBox="0 0 118 88" aria-label="Add task">
    <rect x="2" y="2" width="114" height="84" rx="14" fill="#2a2a2a" stroke="#f2f2f2" stroke-width="3"/>
    <rect x="30" y="40" width="58" height="9" rx="2" fill="#f2f2f2"/>
    <rect x="54.5" y="15" width="9" height="58" rx="2" fill="#f2f2f2"/>
  </svg>

  <footer class="tab-bar">
    <div class="tab" style="left:5px">
      <svg width="56" height="66" viewBox="0 0 56 66">
        <path d="M6 4 H46 L50 62 H10 Z" fill="#3a3a3a" stroke="#888" stroke-width="3"/>
        <path d="M14 18 H42 M15 28 H43 M16 38 H44 M17 48 H45" stroke="#aaa" stroke-width="4"/>
      </svg>
      <span class="tab-label">LIST</span>
    </div>
    <div class="tab is-active" style="left:204px">
      <svg width="56" height="66" viewBox="0 0 56 66">
        <path d="M18 4 H50 L40 62 H6 Z" fill="none" stroke="var(--tab-accent)" stroke-width="3"/>
        <path d="M16 38 L24 48 L40 16" stroke="var(--tab-accent)" stroke-width="3" fill="none"/>
      </svg>
      <span class="tab-label">TASK</span>
    </div>
    <div class="tab" style="left:405px">
      <svg width="56" height="66" viewBox="0 0 56 66">
        <path d="M8 6 L40 2 L48 58 L16 62 Z" fill="#3a3a3a" stroke="#888" stroke-width="3"/>
        <path d="M17 18 L38 15 M18 27 L39 24 M19 36 L40 33 M20 45 L41 42" stroke="#999" stroke-width="3"/>
      </svg>
      <span class="tab-label">NOTE</span>
    </div>
    <div class="tab" style="left:605px">
      <svg width="56" height="66" viewBox="0 0 56 66">
        <circle cx="28" cy="32" r="22" fill="#333" stroke="#888" stroke-width="3"/>
        <path d="M28 20 V44 M16 32 H40" stroke="#aaa" stroke-width="4"/>
      </svg>
      <span class="tab-label">MORE</span>
    </div>
  </footer>

</div>
</body>
</html>
```